Flyer for the Lumen 2025 Conference

I am looking to produce a flyer for our upcoming conference, Lumen 2025. This is an annual conference that we plan to publicize on social media. The ideal designer will create a flyer that is eye-catching and effectively communicates the key information. Please see attached our logo, speaker photo, and flyer content.

Target Market(s)

All demographics

Industry/Entity Type

Christian

Font styles to use
Sans Serif

Requirements
Should not have
• Cross, church

```html
<!DOCTYPE html>
<html lang="en">
<head>
<meta charset="utf-8">
<title>Lumen 2025 Conference Flyer</title>
<link rel="stylesheet" href="https://fonts.googleapis.com/css2?family=Anton&family=Oswald:wght@200;500;600&family=Roboto+Condensed:ital,wght@0,300;0,400;1,300;1,400&family=Roboto:ital,wght@0,400;0,500;0,700;1,400;1,700;1,900&display=swap">
<style>
  :root {
    --stage: #8a8a9c;
    --navy-deep: #050c18;
    --navy-mid: #0b1d33;
    --navy-glow: #163b5e;
    --orange: #f39425;
    --cream: #f4f0d4;
    --white: #ffffff;
    --ink: #101522;
    --frame: #d9dde6;
    --suit-blue: #1f5fb0;
    --suit-dark: #0e2a55;
    --pin-blue: #1c4f96;
  }
  * { margin: 0; padding: 0; box-sizing: border-box; }
  html, body {
    width: 1200px; height: 1200px; overflow: hidden;
    background: var(--stage);
  }
  .flyer {
    position: absolute; left: 120px; top: 0;
    width: 960px; height: 1200px; overflow: hidden;
    background:
      radial-gradient(circle at 26% 16%, var(--navy-glow) 0%, var(--navy-mid) 30%, var(--navy-deep) 70%);
    font-family: "Roboto", Arial, sans-serif;
    color: var(--white);
  }
  .speaker-photo {
    position: absolute; left: 20px; top: 300px; width: 620px; height: 900px;
  }
  .topic {
    position: absolute; left: 88px; top: 145px; width: 200px; text-align: center;
  }
  .label {
    font-family: "Roboto Condensed", Arial, sans-serif;
    font-style: italic; font-weight: 300;
    color: var(--orange); font-size: 30px; letter-spacing: .5px;
  }
  .topic-title, .speaker-name {
    font-family: "Roboto", Arial, sans-serif; font-weight: 400;
    color: var(--cream); font-size: 21px; line-height: 25px; letter-spacing: 1px;
    margin-top: 6px; white-space: nowrap;
  }
  .brand {
    position: absolute; left: 410px; top: 118px; width: 300px;
    display: flex; align-items: center; justify-content: center; gap: 12px;
  }
  .brand-dot { width: 22px; height: 22px; border-radius: 50%; background: var(--orange); }
  .brand-name {
    font-family: "Roboto", Arial, sans-serif; font-weight: 500;
    font-size: 62px; letter-spacing: 2px; color: var(--white);
  }
  .event-title {
    position: absolute; left: 410px; top: 222px; width: 300px; text-align: center;
    white-space: nowrap;
  }
  .event-name {
    font-family: "Anton", Impact, sans-serif; font-weight: 400;
    font-size: 84px; line-height: 88px; color: var(--white);
  }
  .event-year {
    font-family: "Anton", Impact, sans-serif; font-size: 112px; line-height: 110px; color: var(--orange);
  }
  .event-kind-bold {
    font-family: "Oswald", Arial, sans-serif; font-weight: 600;
    font-size: 46px; line-height: 52px; color: var(--cream); margin-top: 6px;
    letter-spacing: -.5px;
  }
  .event-kind-light {
    font-family: "Oswald", Arial, sans-serif; font-weight: 200;
    font-size: 54px; line-height: 58px; color: var(--cream);
    letter-spacing: -.5px;
  }
  .venue { position: absolute; left: 405px; top: 596px; width: 310px; text-align: center; }
  .venue-name {
    font-style: italic; font-weight: 900; font-size: 20px; line-height: 26px;
    white-space: nowrap;
  }
  .venue-address {
    position: relative; margin-top: 14px;
    font-style: italic; font-weight: 400; font-size: 18px; line-height: 28px;
    white-space: nowrap;
  }
  .pin { position: absolute; right: -24px; top: 2px; width: 24px; height: 36px; }
  .speaker { position: absolute; left: 470px; top: 790px; width: 220px; text-align: center; }
  .schedule {
    position: absolute; left: 762px; top: 90px; width: 160px;
    display: flex; flex-direction: column; gap: 86px;
  }
  .day-card {
    border: 1.5px solid var(--frame); border-radius: 4px;
    height: 206px; padding: 22px 0 0; text-align: center;
    display: flex; flex-direction: column; align-items: center;
  }
  .day-name { font-weight: 700; font-size: 25px; line-height: 27px; }
  .day-month { font-weight: 700; font-size: 19px; line-height: 22px; }
  .day-date { font-weight: 700; font-size: 40px; line-height: 46px; }
  .time {
    background: var(--orange); color: var(--ink);
    font-size: 21px; line-height: 25px; width: 108px; margin-top: 4px;
  }
  .app-note {
    position: absolute; left: 770px; top: 940px; width: 180px; text-align: center;
    font-style: italic; font-size: 19px; line-height: 28px;
  }
  .app-name {
    display: block;
    background: var(--orange); color: var(--ink);
    font-family: "Roboto Condensed", Arial, sans-serif; font-style: italic;
    margin: 2px 0;
  }
  .contact {
    position: absolute; font-size: 18px; letter-spacing: .5px; white-space: nowrap;
  }
  .contact-phone { left: 130px; top: 1138px; font-style: italic; font-weight: 500; }
  .contact-email { left: 420px; top: 1128px; font-style: italic; }
  .contact-web { left: 755px; top: 1118px; font-style: italic; }
</style>
</head>
<body>
  <main class="flyer">
    <svg class="speaker-photo" role="img" aria-label="Portrait of the speaker seated in a bright blue suit and grey turtleneck" viewBox="0 0 620 900">
      <defs>
        <radialGradient id="suitTone" cx="45%" cy="55%" r="60%">
          <stop offset="0%" stop-color="#1f5fb0"/>
          <stop offset="65%" stop-color="#0e2a55"/>
          <stop offset="100%" stop-color="#050c18" stop-opacity="0"/>
        </radialGradient>
      </defs>
      <rect width="620" height="900" fill="url(#suitTone)"/>
    </svg>

    <section class="topic">
      <p class="label">TOPIC</p>
      <p class="topic-title">THE VOICE<br>OF THE LORD</p>
    </section>

    <div class="brand">
      <span class="brand-dot"></span>
      <span class="brand-name">KAVOR</span>
    </div>

    <header class="event-title">
      <h1 class="event-name">LUMEN</h1>
      <p class="event-year">2025</p>
      <p class="event-kind-bold">A PROPHETIC</p>
      <p class="event-kind-light">CONFERENCE</p>
    </header>

    <section class="venue">
      <p class="venue-name">The Harborview Performing<br>Arts Center</p>
      <p class="venue-address">218 Alder Grove Street<br>Brookfield, Maine 04011
        <svg class="pin" viewBox="0 0 24 36" aria-hidden="true">
          <path d="M12 0C5.4 0 0 5.2 0 11.6 0 19.5 12 36 12 36s12-16.5 12-24.4C24 5.2 18.6 0 12 0z" fill="#1c4f96"/>
          <circle cx="12" cy="11.5" r="4.6" fill="#050c18"/>
        </svg>
      </p>
    </section>

    <section class="speaker">
      <p class="label">SPEAKER</p>
      <p class="speaker-name">PROPHET<br>ELIAS MARLOW</p>
    </section>

    <aside class="schedule">
      <div class="day-card">
        <p class="day-name">FRIDAY</p>
        <p class="day-month">December</p>
        <p class="day-date">26TH</p>
        <p class="time">6:30PM</p>
        <p class="time">9:00PM</p>
      </div>
      <div class="day-card">
        <p class="day-name">SATURDAY</p>
        <p class="day-month">December</p>
        <p class="day-date">27TH</p>
        <p class="time">5:30PM</p>
        <p class="time">8:00PM</p>
      </div>
      <div class="day-card">
        <p class="day-name">SUNDAY</p>
        <p class="day-month">December</p>
        <p class="day-date">29TH</p>
        <p class="time">4:30PM</p>
        <p class="time">7:00PM</p>
      </div>
    </aside>

    <p class="app-note">Download the<span class="app-name">KAVOR APP</span>to stay updated on the event</p>

    <p class="contact contact-phone">207 555 0148</p>
    <p class="contact contact-email">contact@kavor.org</p>
    <p class="contact contact-web">www.kavor.org</p>
  </main>
</body>
</html>
```